Tallowmoor Letterheads Design

Hello, we have just upgraded this project for a guaranteed payment.

We are currently going through a re-branding exercise internally. Our logo is attached as a PDF file.

We are happy with our logo but would like to investigate how we can best apply the logo to our letterheads and compliment slips.

We are a quality printing company in England. Despite our name we are very professional and offer a personal service.

Our new website is under construction and here is a link to show you how it looks: http://brackenpress.v4ntor.co.uk

The style must be professional and steer away from "tacky" otherwise it makes our company look very low budget and just a bit silly.

We would like to see elements of creativity though, so please, nothing too boring.

I have attached our new logo, there is an option for use on white or black.

Cheers
Tallowmoor Team

Reason: We have increased the deadline due to an internal delay to things, we now have more time before we need anything to be printed.

Industry/Entity Type

Construction

Requirements
Must have
• IMPORTANT! Please do not tweak or change our logo in any way. A few designs show vast changes in the logo, this is not what we require. Please do not change the logo in any way. Thanks
Nice to have
• Classy but approachable. Elements of "quirky" would be nice to see.
Should not have
• A Tacky feel

```html
<!DOCTYPE html>
<html lang="en">
<head>
<meta charset="utf-8">
<title>Tallowmoor Letterhead</title>
<link href="https://fonts.googleapis.com/css2?family=Arimo:wght@400;700&display=swap" rel="stylesheet">
<style>
  :root {
    --pink-1: #f0287a;
    --pink-2: #f0668c;
    --pink-3: #f291a6;
    --pink-4: #f7b3c0;
    --pink-5: #fbd7dd;
    --pink-6: #fde8eb;
    --ink: #1a1a1a;
    --edge: #8a8a8a;
    --paper: #ffffff;
  }
  html, body {
    margin: 0;
    padding: 0;
    overflow: hidden;
    background: var(--paper);
  }
  .letterhead {
    position: relative;
    width: 927px;
    height: 1200px;
    background: var(--paper);
    box-sizing: border-box;
    border-top: 1px solid var(--edge);
    border-right: 1px solid var(--edge);
    font-family: "Arimo", Arial, sans-serif;
    overflow: hidden;
  }
  .tint-strip {
    position: absolute;
    left: 0;
    top: 0;
    width: 164px;
  }
  .tint {
    position: absolute;
    left: 0;
    width: 164px;
    height: 162px;
  }
  .tint--1 { top: 0;     background: var(--pink-1); }
  .tint--2 { top: 173px; background: var(--pink-2); }
  .tint--3 { top: 345px; background: var(--pink-3); }
  .tint--4 { top: 518px; background: var(--pink-4); }
  .tint--5 { top: 691px; background: var(--pink-5); }
  .tint--6 { top: 863px; background: var(--pink-6); }

  .brand {
    position: absolute;
    left: 0;
    top: 1034px;
    width: 164px;
    text-align: center;
  }
  .brand__mark {
    display: block;
    width: 40px;
    height: 40px;
    margin: 0 auto 4px;
    border-radius: 50%;
    background: var(--pink-1);
  }
  .brand__name {
    font-size: 24px;
    font-weight: 700;
    color: var(--ink);
    letter-spacing: -0.5px;
    line-height: 1;
  }
  .brand__tagline {
    font-size: 9px;
    font-weight: 700;
    color: var(--ink);
    margin-top: 2px;
    line-height: 1;
  }
  .contact {
    position: absolute;
    left: 12px;
    top: 1124px;
    color: var(--pink-1);
    font-weight: 700;
    line-height: 1;
  }
  .contact__web   { font-size: 17px; margin-bottom: 5px; }
  .contact__phone { font-size: 18px; letter-spacing: 1.4px; margin-bottom: 4px; }
  .contact__email { font-size: 12px; font-weight: 400; }
</style>
</head>
<body>
  <main class="letterhead">
    <div class="tint-strip">
      <div class="tint tint--1"></div>
      <div class="tint tint--2"></div>
      <div class="tint tint--3"></div>
      <div class="tint tint--4"></div>
      <div class="tint tint--5"></div>
      <div class="tint tint--6"></div>
    </div>

    <div class="brand">
      <span class="brand__mark"></span>
      <div class="brand__name">Tallowmoor</div>
      <div class="brand__tagline">Quality Printing</div>
    </div>

    <address class="contact" style="font-style: normal;">
      <div class="contact__web">tallowmoor.co.uk</div>
      <div class="contact__phone">0208 555 0192</div>
      <div class="contact__email">sales@tallowmoor.co.uk</div>
    </address>
  </main>
</body>
</html>
```